Relaunch / redesign online store

We want to refresh our existing online store and have a clear, bright, modern and disgusting template. We are running an online store for fireplaces and chimneys. Our positioning in the market is recognized as a specialist for fireplaces. Due to the fact that the products are costy, we need to send the message that we are trustful. The goal is to make the page look fresh and modern again, without being too posh. In the actual desing there are too many elements like sliders, etc. It is overloaded with information and may overwhelm the user. The elements given in the header and footer, etc. Elements that you can delete are: Tile with "Sure because certified "In it," Save coupon now "," our top sellers for you ", Elements under" Worth knowing ". The store has several types of landing pages. Here is an example for each type of landing page: Home: kolvaro.de Category: https://www.kolvaro.de/kaminofen Product: https://www.kolvaro.de/kaminofen/kaminofen-varnel-dorvin-6 -kw.html Content: https://www.kolvaro.de/kaminofen-aufbauservice-anschluss Please give us an idea of every landing page type. Think about the mobile look of the design. The design has become easy to use for a responsive template. The clickable elements as links, buttons, etc. have to be enough and clear to recognize by the user. Generally speaking, we want to make the site kolvaro.de look up to date again. The actual design is about 10 years old. A modern template should use more of the width of screens. So, the left, font size etc. should be bigger and more up to date looking. So, the design should be less dark than it is now. The colors used for the new look should match the logo color and style but we are not narrowed to some special colors. Here you have space for creativity. Here are some keywords which should match your design: cozy, warm, professional, clear, good price-performance ratio, trustful, state of the art, our target group is 45 years of age. We are looking forward to your design.

Target Market(s)

germany

Number of Pages Required

4 page

Requirements
Must have
• The elements like menu structre, links and content on the pages have as a part of the new design. The sliders are now on the main home can be completely deleted.

```html
<!DOCTYPE html>
<html lang="en">
<head>
<meta charset="utf-8">
<title>kolvaro – Fireplaces Online</title>
<link href="https://fonts.googleapis.com/css2?family=Roboto:wght@400;500;700&family=Roboto+Condensed:wght@400;700&display=swap" rel="stylesheet">
<style>
:root{
  --orange:#f39200;
  --orange-dark:#d97e00;
  --ink:#2b2b2b;
  --muted:#8a8a8a;
  --line:#e4e4e4;
  --soft:#f6f6f6;
  --peach:#fdf0e2;
  --footer:#2a2624;
  --footer-text:#b9b2ac;
  --white:#ffffff;
}
*{box-sizing:border-box;margin:0;padding:0}
html,body{width:1200px;height:2992px;overflow:hidden}
body{position:relative;background:var(--white);font-family:"Roboto",Arial,sans-serif;color:var(--ink)}
.abs{position:absolute}
.section-title{position:absolute;left:0;width:1200px;text-align:center;font-family:"Roboto Condensed",Arial,sans-serif;font-weight:700;font-size:36px;color:var(--orange)}
.section-title::after{content:"";display:block;width:60px;height:3px;margin:10px auto 0;background:var(--orange);border-radius:2px}
.btn{position:absolute;display:block;background:var(--orange);color:var(--white);font-size:14px;font-weight:500;text-align:center;border-radius:3px;text-decoration:none}

/* hero */
.hero{position:absolute;left:0;top:0;width:1200px;height:580px;overflow:hidden}
.hero-photo{position:absolute;inset:0;background:radial-gradient(ellipse at 75% 55%,#d9a27a 0%,#9a5a34 30%,#4a2718 62%,#1f120c 100%)}
.hero-shade{position:absolute;inset:0;background:linear-gradient(90deg,rgba(20,10,5,.6) 0%,rgba(20,10,5,.1) 60%)}
.logo{position:absolute;left:40px;top:34px;display:flex;align-items:center;gap:10px;color:var(--white);font-size:30px;font-weight:700}
.logo-mark{width:22px;height:22px;background:var(--orange);border-radius:50%}
.main-nav{position:absolute;left:590px;top:44px;display:flex;gap:30px;font-size:14px;color:var(--white)}
.search{position:absolute;left:960px;top:36px;width:200px;height:34px;border:1px solid rgba(255,255,255,.8);border-radius:3px;color:rgba(255,255,255,.75);font-size:13px;padding:8px 12px}
.hero h1{position:absolute;left:248px;top:190px;font-size:44px;line-height:52px;font-weight:500;color:var(--white)}
.hero p{position:absolute;left:248px;top:304px;width:330px;font-size:12px;line-height:18px;color:rgba(255,255,255,.85)}
.hero .btn{left:248px;top:366px;width:140px;height:36px;line-height:36px}
.hero-wave{position:absolute;left:0;top:0}

/* benefits */
.benefits{position:absolute;left:0;top:580px;width:1200px;height:320px}
.benefit{position:absolute;top:120px;width:170px;text-align:center}
.benefit-icon{width:76px;height:76px;margin:0 auto;background:var(--orange);border-radius:50%;display:flex;align-items:center;justify-content:center}
.benefit h3{margin-top:18px;font-size:14px;font-weight:700}
.benefit p{margin-top:10px;font-size:11px;line-height:16px;color:var(--muted)}

/* products */
.products{position:absolute;left:0;top:910px;width:1200px;height:420px;background:var(--soft)}
.product-tile{position:absolute;top:160px;width:88px;text-align:center}
.product-thumb{width:88px;height:88px;background:var(--white);border:1px solid var(--line);display:flex;align-items:center;justify-content:center}
.product-thumb span{display:block;width:60px;height:62px;border-radius:4px}
.product-tile p{margin-top:14px;font-size:13px;font-weight:500}
.products .btn{left:540px;top:330px;width:120px;height:34px;line-height:34px}

/* story */
.story{position:absolute;left:0;top:1340px;width:1200px;height:570px;background:linear-gradient(90deg,#eceae7 0%,#f7f6f4 60%,#fff 100%)}
.story-photo{position:absolute;left:0;top:0;width:620px;height:570px;background:radial-gradient(ellipse at 45% 40%,#d8c4b3 0%,#b48e74 30%,#7b6150 55%,#dcd8d2 100%)}
.story h2{position:absolute;left:580px;top:60px;width:470px;font-size:27px;line-height:34px;font-weight:400;color:var(--ink)}
.story-list{position:absolute;left:580px;top:186px;width:520px;list-style:none}
.story-list li{margin-bottom:22px}
.story-list h4{font-size:14px;font-weight:700;color:var(--orange);display:flex;align-items:center;gap:8px}
.story-list h4 i{display:inline-block;width:14px;height:14px;border-radius:50%;background:var(--orange)}
.story-list p{margin-top:6px;font-size:11px;line-height:16px;color:#666}

/* top quality */
.quality{position:absolute;left:0;top:1920px;width:1200px;height:470px}
.quality .section-title span{color:var(--ink);font-weight:400}
.offer-card{position:absolute;top:118px;width:212px;height:230px;background:var(--white);border:1px solid var(--line);box-shadow:0 2px 8px rgba(0,0,0,.06);padding:14px}
.offer-photo{width:184px;height:110px;background:linear-gradient(180deg,#e9e6e2 0%,#2e2a27 25%,#1b1816 70%,#cfcac4 100%)}
.offer-card h5{margin-top:14px;font-size:11px;line-height:15px;font-weight:500;text-align:center}
.offer-card .price{margin-top:10px;text-align:center;font-size:14px;font-weight:700;color:var(--orange)}
.offer-card .price s{font-size:11px;font-weight:400;color:var(--muted);margin-right:6px}
.arrow{position:absolute;top:210px}
.quality .btn{left:545px;top:410px;width:110px;height:32px;line-height:32px}

/* brands */
.brands{position:absolute;left:0;top:2400px;width:1200px;height:330px;background:var(--peach)}
.brand-row{position:absolute;left:220px;top:148px;width:760px;display:flex;justify-content:space-between;align-items:center}
.brand-row span{display:flex;align-items:center;gap:6px;font-size:17px;font-weight:500;color:#555}
.brand-row span i{display:inline-block;width:12px;height:12px;border-radius:50%;background:#888}

/* footer */
.footer{position:absolute;left:0;top:2640px;width:1200px;height:352px}
.footer-bg{position:absolute;left:0;top:0}
.footer-col{position:absolute;top:90px;font-size:11px;line-height:19px;color:var(--footer-text)}
.footer-col h6{font-size:14px;font-weight:700;color:var(--orange);margin-bottom:10px}
.pay-row{display:flex;gap:8px;margin-bottom:8px}
.pay-row b{display:block;width:52px;height:30px;background:#e8e4e0;border-radius:3px}
.bottom-bar{position:absolute;left:0;top:296px;width:1200px;height:56px;border-top:1px solid rgba(255,255,255,.12)}
.bottom-bar .copy{position:absolute;left:232px;top:18px;font-size:11px;color:var(--orange)}
.bottom-bar .legal{position:absolute;left:470px;top:12px;width:300px;text-align:center;font-size:9px;line-height:13px;color:var(--footer-text)}
.socials{position:absolute;left:880px;top:14px;display:flex;gap:8px}
.socials b{display:block;width:24px;height:24px;background:#6c6662;border-radius:3px}
</style>
</head>
<body>

<header class="hero">
  <div class="hero-photo" role="img" aria-label="Mother and daughter cuddling in front of a glowing fireplace in a cozy living room"></div>
  <div class="hero-shade"></div>
  <div class="logo"><span class="logo-mark"></span>kolvaro</div>
  <nav class="main-nav"><span>Home</span><span>About Us</span><span>Our Products</span><span>Contact Us</span></nav>
  <div class="search">Search…</div>
  <h1>Get your shopping<br>into an experience</h1>
  <p>Discover warm fireplaces, stoves and chimneys chosen by specialists. Fair prices, honest advice and fast delivery to your door.</p>
  <a class="btn">Discover Products</a>
  <svg class="hero-wave" width="1200" height="580" viewBox="0 0 1200 580">
    <path d="M0 468 C260 560 620 610 880 530 C1010 490 1110 430 1200 420 L1200 580 L0 580 Z" fill="#ffffff"/>
  </svg>
</header>

<section class="benefits">
  <h2 class="section-title" style="top:20px">Our Benefits</h2>
  <div class="benefit" style="left:227px">
    <div class="benefit-icon"><svg width="38" height="30" viewBox="0 0 38 30" fill="none" stroke="#fff" stroke-width="2.4"><rect x="2" y="6" width="20" height="15"/><path d="M22 11h8l5 5v5H22"/><circle cx="9" cy="24" r="3"/><circle cx="29" cy="24" r="3"/></svg></div>
    <h3>Free Shipping</h3>
    <p>Free delivery within Germany on every order, packed safely and tracked until it reaches you.</p>
  </div>
  <div class="benefit" style="left:415px">
    <div class="benefit-icon"><svg width="34" height="34" viewBox="0 0 34 34" fill="none" stroke="#fff" stroke-width="2.4"><rect x="6" y="4" width="22" height="26" rx="2"/><rect x="11" y="14" width="12" height="10"/><path d="M11 9h12"/></svg></div>
    <h3>Stove Connection</h3>
    <p>Our certified partners install and connect your stove quickly, cleanly and fully to standard.</p>
  </div>
  <div class="benefit" style="left:603px">
    <div class="benefit-icon"><svg width="34" height="34" viewBox="0 0 34 34" fill="none" stroke="#fff" stroke-width="2.4"><path d="M17 3l12 5v9c0 7-5 12-12 14C10 29 5 24 5 17V8z"/><path d="M11 17l4 4 8-8"/></svg></div>
    <h3>Safe Checkout Guaranteed</h3>
    <p>Pay securely with encrypted checkout and trusted payment methods you already know well.</p>
  </div>
  <div class="benefit" style="left:791px">
    <div class="benefit-icon"><svg width="34" height="34" viewBox="0 0 34 34" fill="none" stroke="#fff" stroke-width="2.4"><circle cx="17" cy="17" r="13"/><path d="M17 9v8l6 4"/></svg></div>
    <h3>Chimney Planning Made Easy</h3>
    <p>Plan your complete chimney system online with expert help from our specialist team.</p>
  </div>
</section>

<section class="products">
  <h2 class="section-title" style="top:66px">Our Products</h2>
  <div class="product-tile" style="left:231px"><div class="product-thumb"><span role="img" aria-label="Wood stove" style="background:linear-gradient(#4a4440,#1f1c1a)"></span></div><p>Stoves</p></div>
  <div class="product-tile" style="left:361px"><div class="product-thumb"><span role="img" aria-label="Wood pellets" style="background:linear-gradient(#c9a774,#8c6a3c)"></span></div><p>Pellet</p></div>
  <div class="product-tile" style="left:491px"><div class="product-thumb"><span role="img" aria-label="Chimney pipes" style="background:linear-gradient(90deg,#9a9a9a,#dcdcdc,#8c8c8c)"></span></div><p>Chimney</p></div>
  <div class="product-tile" style="left:621px"><div class="product-thumb"><span role="img" aria-label="Charcoal grill" style="background:linear-gradient(#333,#111)"></span></div><p>Grilling</p></div>
  <div class="product-tile" style="left:751px"><div class="product-thumb"><span role="img" aria-label="Fireplace insert" style="background:linear-gradient(#5a5450,#2a2624)"></span></div><p>Substitutes</p></div>
  <div class="product-tile" style="left:881px"><div class="product-thumb"><span role="img" aria-label="Fireplace equipment" style="background:linear-gradient(#b7b2ad,#6e6864)"></span></div><p>Equipment</p></div>
  <a class="btn">View Products</a>
</section>

<section class="story">
  <div class="story-photo" role="img" aria-label="Man in an apron grilling meat outdoors"></div>
  <h2>Buy your fireplace conveniently online at kolvaro You will find your dream fireplaces</h2>
  <ul class="story-list">
    <li><h4><i></i>Personal fireplace consultation</h4><p>Our specialists help you choose the right stove for your room size, heating needs and style, by phone or e-mail, free of charge and without obligation.</p></li>
    <li><h4><i></i>Fair prices you can rely on</h4><p>We work directly with leading manufacturers, so you get quality products at a strong price-performance ratio and transparent costs from the start.</p></li>
    <li><h4><i></i>Certified quality for a safe home</h4><p>Every stove and chimney we sell meets current German emission and safety standards, tested and approved for long, worry-free use in your home.</p></li>
    <li><h4><i></i>Delivery and installation</h4><p>We deliver free of charge and arrange setup and connection through trusted local partners, so your new fireplace is ready to warm you quickly.</p></li>
  </ul>
</section>

<section class="quality">
  <h2 class="section-title" style="top:20px">Top Quality-<span>Better Life</span></h2>
  <svg class="arrow" style="left:180px" width="14" height="24" viewBox="0 0 14 24"><path d="M12 2L2 12l10 10" fill="none" stroke="#999" stroke-width="2"/></svg>
  <div class="offer-card" style="left:228px"><div class="offer-photo" role="img" aria-label="Built-in fireplace insert with glass door"></div><h5>Fireplace insert Varnel series, 45/55 front panel, 9 kW heating output</h5><p class="price"><s>€ 2.499,00</s>€ 2.190,00</p></div>
  <div class="offer-card" style="left:480px"><div class="offer-photo" role="img" aria-label="Built-in fireplace insert with glass door"></div><h5>Fireplace insert Varnel series, 45/55 front panel, 9 kW heating output</h5><p class="price"><s>€ 2.499,00</s>€ 2.190,00</p></div>
  <div class="offer-card" style="left:732px"><div class="offer-photo" role="img" aria-label="Built-in fireplace insert with glass door"></div><h5>Fireplace insert Varnel series, 45/55 front panel, 9 kW heating output</h5><p class="price"><s>€ 2.499,00</s>€ 2.190,00</p></div>
  <svg class="arrow" style="left:1000px" width="14" height="24" viewBox="0 0 14 24"><path d="M2 2l10 10L2 22" fill="none" stroke="#999" stroke-width="2"/></svg>
  <a class="btn">Read More</a>
</section>

<section class="brands">
  <h2 class="section-title" style="top:60px">Our Brands</h2>
  <div class="brand-row">
    <span><i></i>Halvern</span><span><i></i>Nordtal</span><span><i></i>Brasko</span><span>Vestora</span><span><i></i>Feldmann</span><span><i></i>Ostrun</span>
  </div>
</section>

<footer class="footer">
  <svg class="footer-bg" width="1200" height="352" viewBox="0 0 1200 352">
    <path d="M0 40 C300 -10 600 90 900 40 C1020 20 1120 30 1200 50 L1200 352 L0 352 Z" fill="#2a2624"/>
  </svg>
  <div class="footer-col" style="left:232px"><h6>Information</h6>Shipping and delivery<br>Payment options<br>Terms and conditions<br>Right of withdrawal<br>Privacy policy<br>Imprint<br>Customer account</div>
  <div class="footer-col" style="left:362px;top:119px">Stove installation<br>Chimney planning<br>Fireplace accessories<br>Pellet stoves guide<br>Safety and standards<br>Returns and refunds<br>Frequently asked</div>
  <div class="footer-col" style="left:560px"><h6>Address &amp; Contact</h6>kolvaro GmbH<br>Lindenweg 14<br>30159 Musterstadt<br>Phone: 0511 000 4712<br>E-mail: service@kolvaro.de<br>Mon–Fri 8:00 – 18:00</div>
  <div class="footer-col" style="left:832px"><h6>Payment and Shipping</h6><div class="pay-row"><b></b><b></b><b></b></div><div class="pay-row"><b></b><b></b></div></div>
  <div class="bottom-bar">
    <p class="copy">© 2024 kolvaro.de, all rights reserved</p>
    <p class="legal">All prices include VAT plus shipping costs where stated.<br>Offers valid while stocks last, errors excepted.</p>
    <div class="socials"><b></b><b></b><b></b></div>
  </div>
</footer>

</body>
</html>
```